Community Bank Web Design

Design a homepage and internal product page for a community bank. Needs to be mobile friendly, minimal scrolling on home. Create the homepage look & feel, then use the same aesthetic to create the product page for the personal checking account page.

Wireframes, logo variations, and color scheme attached.

New brand identity:
• Open, Fresh, Younger, Bright, Bold, New, Innovative.
• Inviting, approachable, friendly, trustworthy.
• Imagine a young family purchasing their first home as the target audience.
You do not have to stick to the exact layout of the wireframes, as long as all of the elements are present.

All navigation elements are specified in wireframes. There are three versions of the homepage – Personal Home, Business Home, Wealth Management Home – you may design whichever version you prefer.

For internal page – please design the Checking product page, included in wireframes.

NOTE: Submit your homepage design first. I will provide feedback on your design direction, then you can use that to move forward with the internal page design.

Design direction--
Some banking / financial sites we like for their fresh/bold/open look:
velmorant.com
quastel.ca
rpwfinancial.org
kdh.co.nz
yarbel.com
pettigrubank.com
uvm.co.nz

Target Market(s)

The target market for the personal homepage varies. Adults in the midwest, 25 - 60, who are striving to build their savings and manage their money. Often buying homes or refinancing their homes to make renovations, or planning for retirement.

For the business homepage, the target market are small to mid-market business owners striving to grow their business and manage their company.

Industry/Entity Type

Financial

Requirements
Must have
• colors: CRIMSON #a20c33,
FOREST GREEN #004f38
GOLD #e6a513

File format for design submission must be layered PSD (Please organize layers into recognizable folders like "menu" and "footer")

To make the design "mobile friendly" please create a grid-based layout. http://www.dorvané.com/patterns/showPattern.php?patternID=grid-based-layout
http://www.brindlequarterly.com/2007/04/14/designing-with-grid-based-approach/

```html
<!DOCTYPE html>
<html lang="en">
<head>
<meta charset="utf-8">
<title>Harrow Creek Bank</title>
<link href="https://fonts.googleapis.com/css2?family=Arimo:wght@400;700&display=swap" rel="stylesheet">
<style>
:root{
  --crimson:#a20c33;
  --gold:#fcc12e;
  --dark:#383838;
  --panel-line:#6a6a6a;
  --text:#333;
  --muted:#8a8a8a;
  --line:#dcdcdc;
}
*{box-sizing:border-box;margin:0;padding:0}
html,body{width:1200px;height:1190px;overflow:hidden;background:#fff}
body{font-family:Arimo,Arial,sans-serif;color:var(--text)}
.page{position:relative;width:1280px;height:1269px;transform:scale(.9375);transform-origin:0 0}
.abs{position:absolute}
.top-rule{left:0;top:0;width:1280px;height:4px;background:var(--crimson)}
.brand{left:150px;top:38px;display:flex;align-items:center;gap:10px}
.brand-mark{width:40px;height:40px;border-radius:50%;background:var(--crimson)}
.brand-name{font-size:25px;color:var(--crimson);font-weight:400}
.search{left:859px;top:40px;width:291px;height:43px;border:1px solid var(--line);display:flex;align-items:center;justify-content:space-between;padding:0 12px;font-size:12px;color:#555}
.nav{left:150px;top:116px;width:1000px;height:66px;border:1px solid var(--line);background:linear-gradient(#f6f6f6,#e4e4e4)}
.nav-item{position:absolute;top:10px;text-align:center;font-size:15px;line-height:24px;color:#555}
.nav-sep{position:absolute;top:10px;width:1px;height:46px;background:#d0d0d0}
.login-btn{position:absolute;left:868px;top:9px;width:115px;height:45px;background:var(--crimson);color:#fff;display:flex;align-items:center;justify-content:center;gap:12px;font-size:16px}
.login-panel{left:150px;top:200px;width:347px;height:412px;background:var(--dark)}
.login-inner{position:absolute;left:9px;top:9px;width:329px;height:394px;border:1px solid var(--panel-line);color:#fff}
.field{position:absolute;left:14px;width:298px;height:45px;border:1px solid var(--panel-line);font-size:15px;display:flex;align-items:center;padding-left:12px}
.gold-btn{background:var(--gold);color:#3a2c00;font-weight:700;display:flex;align-items:center;justify-content:center}
.hero{left:505px;top:200px;width:644px;height:411px;background:radial-gradient(circle at 30% 30%,#eef4f8,#bcd2df 45%,#8fb0c2 75%,#5d8aa3)}
.hero-bar{position:absolute;left:0;bottom:0;width:100%;height:63px;background:rgba(70,70,70,.8);color:#fff;font-size:15px}
.feature-img{left:150px;top:637px;width:237px;height:220px;background:linear-gradient(135deg,#dfe7ee,#9fb3c3 55%,#5f7586)}
.feature{left:410px;top:636px;width:440px}
.feature h2{font-size:18px;font-weight:400;color:#222;margin-bottom:12px}
.feature p{font-size:12px;line-height:26px;color:var(--muted)}
.rates{left:865px;top:637px;width:285px;height:220px;border:2px solid #e6e6e6}
.rates h3{position:absolute;left:97px;top:22px;font-size:20px;font-weight:400;color:var(--crimson)}
.rates p{position:absolute;left:97px;top:52px;width:170px;font-size:12px;line-height:23px;color:var(--muted)}
.card{top:923px;width:325px;height:186px;border:1px solid var(--line)}
.card h4{position:absolute;left:11px;top:16px;font-size:14px;font-weight:400;color:var(--crimson)}
.card p{position:absolute;left:10px;top:46px;width:200px;font-size:12px;line-height:24px;color:var(--muted)}
.card .icon-box{position:absolute;left:216px;top:49px;width:95px;height:91px;border:1px solid #ccc;display:flex;align-items:center;justify-content:center}
.card a{position:absolute;left:11px;top:152px;font-size:14px;color:var(--crimson);text-decoration:none}
.footer{left:0;top:1140px;width:1280px;height:129px;background:var(--dark);color:#fff;font-size:12px}
.social{position:absolute;top:78px;width:29px;height:29px;border:2px solid #fff;border-radius:50%}
</style>
</head>
<body>
<div class="page">
  <div class="abs top-rule"></div>

  <div class="abs brand"><span class="brand-mark"></span><span class="brand-name">Harrow Creek Bank</span></div>

  <div class="abs search"><span>Enter Any Keyword.......</span>
    <svg width="16" height="16" viewBox="0 0 16 16"><circle cx="6.5" cy="6.5" r="5" fill="none" stroke="#999" stroke-width="2"/><line x1="10" y1="10" x2="15" y2="15" stroke="#999" stroke-width="2.5"/></svg>
  </div>

  <nav class="abs nav">
    <div class="nav-item" style="left:22px;width:102px">Products &amp;<br>Services</div>
    <div class="nav-sep" style="left:151px"></div>
    <div class="nav-item" style="left:178px;width:80px;top:11px">Why<br>HCB?</div>
    <div class="nav-sep" style="left:283px"></div>
    <div class="nav-item" style="left:310px;width:100px;top:11px">Customer<br>Center</div>
    <div class="login-btn">
      <svg width="20" height="24" viewBox="0 0 20 24"><path d="M5 10V7a5 5 0 0 1 10 0v3" fill="none" stroke="#fff" stroke-width="2.5"/><rect x="1" y="10" width="18" height="13" rx="2" fill="#fff"/><rect x="9" y="14" width="2" height="5" fill="#a20c33"/></svg>
      LOG IN
    </div>
  </nav>

  <section class="abs login-panel">
    <div class="login-inner">
      <div class="abs" style="left:14px;top:26px;font-size:15px">ACCOUNT TYPE</div>
      <div class="field" style="top:51px">Banking
        <span style="position:absolute;right:0;top:0;width:43px;height:43px;border-left:1px solid var(--panel-line);display:flex;align-items:center;justify-content:center">
          <svg width="12" height="9"><path d="M0 0h12L6 9z" fill="#fff"/></svg></span>
      </div>
      <div class="field" style="top:108px">User ID</div>
      <div class="abs" style="left:15px;top:163px;font-size:12px">Forgot User ID ?</div>
      <div class="abs gold-btn" style="left:17px;top:185px;width:134px;height:41px;gap:18px;font-size:16px">
        <svg width="18" height="22" viewBox="0 0 20 24"><path d="M5 10V7a5 5 0 0 1 10 0v3" fill="none" stroke="#333" stroke-width="2.5"/><rect x="1" y="10" width="18" height="13" rx="2" fill="#333"/><rect x="9" y="14" width="2" height="5" fill="#fcc12e"/></svg>
        LOGIN</div>
      <div class="abs" style="left:18px;top:244px;font-size:15px">NEW TO HCB ONLINE?</div>
      <div class="field" style="top:275px;left:15px;font-size:12px">ENROLL , LEARN MORE</div>
      <div class="abs" style="left:38px;top:338px;width:251px;height:43px;background:#e6ebf8;color:#666;font-weight:700;font-size:17px;display:flex;align-items:center;justify-content:center">Apply For a loan</div>
    </div>
  </section>

  <section class="abs hero" role="img" aria-label="Photo of hands typing on a laptop keyboard">
    <svg class="abs" style="left:16px;top:158px" width="24" height="66"><path d="M21 2 4 33l17 31" fill="none" stroke="#777" stroke-width="3"/></svg>
    <svg class="abs" style="left:594px;top:158px" width="24" height="66"><path d="M3 2l17 31L3 64" fill="none" stroke="#777" stroke-width="3"/></svg>
    <div class="hero-bar">
      <span class="abs" style="left:18px;top:25px">Rotating Promotional Messaging - Ties to Rotating Large Graphic</span>
      <span class="abs gold-btn" style="left:470px;top:11px;width:157px;height:42px;font-size:16px">LEARN MORE</span>
    </div>
  </section>

  <div class="abs feature-img" role="img" aria-label="Photo of a hand using a smartphone beside a coffee cup"></div>

  <section class="abs feature">
    <h2>Home&nbsp; Equity Lines Of Credit</h2>
    <p>Creek Bank you are making a personal choice, and you are rewarded with over 100 years experience in incredible personal service. From business loans and financial planning, to online banking, our options will surprise you. Visit one of our locations and put your trust in a community bank that truly understands customer needs by delivering a product that is right for you. Find out why our personal approach to banking has our customers saying needs by delivering a product that Find out why our personal approach to banking has saying.......</p>
  </section>

  <section class="abs rates">
    <svg class="abs" style="left:8px;top:56px" width="82" height="80" viewBox="0 0 82 80"><path d="M41 2l10 28h30L57 48l9 30-25-18-25 18 9-30L1 30h30z" fill="#f0c232" stroke="#d9a514" stroke-width="1.5"/></svg>
    <h3>Rates</h3>
    <p>Creek Bank you are making a personal choice, and you are rewarded with over 100 years personal service.........</p>
    <div class="abs gold-btn" style="left:100px;top:158px;width:136px;height:41px;font-size:14px">VIEW RATES</div>
  </section>

  <section class="abs card" style="left:149px">
    <h4>Mobile Deposit.It's Easy!</h4>
    <p>When you choose Harrow Creek Bank you are making a personal choice, and you are rewarded with incredible personal service...........</p>
    <div class="icon-box"><svg width="58" height="58" viewBox="0 0 58 58"><rect x="6" y="4" width="26" height="50" rx="4" fill="none" stroke="#6e6e6e" stroke-width="5"/><path d="M22 22l16 0 14 12-10 12H30l-8-10z" fill="#6e6e6e"/></svg></div>
    <a href="#">[ LEARN MORE ]</a>
  </section>
  <section class="abs card" style="left:486px">
    <h4>Looking For a New Home?</h4>
    <p>When you choose Harrow Creek Bank you are making a personal choice, and you are rewarded with incredible personal service...........</p>
    <div class="icon-box"><svg width="56" height="50" viewBox="0 0 56 50"><path d="M28 3 2 27h8v21h13V34h10v14h13V27h8z" fill="#6e6e6e"/></svg></div>
    <a href="#">[ Find Your Mortgage Banker ]</a>
  </section>
  <section class="abs card" style="left:824px">
    <h4>Corvo Debit Cards</h4>
    <p>When you choose Harrow Creek Bank you are making a personal choice, and you are rewarded with incredible personal service...........</p>
    <div class="icon-box"><svg width="74" height="58" viewBox="0 0 74 58"><rect x="16" y="4" width="54" height="34" rx="3" fill="#8a8a8a" transform="rotate(-12 43 21)"/><rect x="2" y="18" width="58" height="36" rx="3" fill="#6e6e6e"/><text x="24" y="32" font-size="10" font-family="Arimo,sans-serif" font-weight="700" fill="#fff">BANK</text><rect x="8" y="26" width="9" height="7" fill="#ddd"/><text x="8" y="48" font-size="6" font-family="Arimo,sans-serif" fill="#ddd">1234 5678</text></svg></div>
    <a href="#">[ LEARN MORE ]</a>
  </section>

  <footer class="abs footer">
    <div class="abs" style="left:151px;top:35px">Products &amp; Services &nbsp;&nbsp;&nbsp;&nbsp;|&nbsp;&nbsp;&nbsp;&nbsp; Why HCB? &nbsp;&nbsp;&nbsp;&nbsp;|&nbsp;&nbsp;&nbsp;&nbsp; Customer Center</div>
    <div class="abs" style="left:151px;top:80px">Copy Rights 2014 Harrow Creek Bank.All Rights Reseved.</div>
    <div class="abs" style="left:1024px;top:20px;display:flex;align-items:center;gap:8px"><span style="width:34px;height:34px;border-radius:50%;background:#fff"></span><span style="font-size:16px;line-height:17px">Harrow Creek<br>Bank</span></div>
    <span class="social" style="left:972px"></span>
    <span class="social" style="left:1010px"></span>
    <span class="social" style="left:1046px"></span>
    <span class="social" style="left:1083px"></span>
    <span class="social" style="left:1119px"></span>
    <div class="abs" style="left:1180px;top:95px">C2</div>
  </footer>
</div>
</body>
</html>
```